Company brochure for our unique consulting business

We are a small consulting business offering a unique set of services to our clients.. In simple terms we are a business improvement consultancy helping our clients get the best out of their businesses. We work with clients across multiple sectors and deliver a variety of services. We want to put together a brochure to cover these main themes:1. Who we are2. What we do3. The type of people we employ4. The sectors we work inWhile the brochure needs to have a certain corporate feel to it, we don't want it to be "boring" or "stiff". We would like it to have a slightly "friendly" or "informal" feel to it, to reflect the type of organisation we are.We have a company website http://tollandvergeadvisory.com , however we do not want to directly replicate the content or feel as we recognise it needs updating.We would like the brochure to be A4 portrait format. We anticipate requiring 12 sides (including covers) but we are happy to be guided on this based on the content we have provided.The attached ppt file gives the detail of the content to be included and also shows the proposed pagination. For the front cover we would like to try 2 versions, one with the TVA logo and one with the Tolland Verge Advisory logo (a file of both is attached)One of the most important pages will be the "Our Services" page. We would like this to cover the centre fold. In the ppt file we have shown an example layout, but this is where we need most help - we are clearly not graphic designers! This page will be the most used page in sales meetings etc.Also attached is the following:1. file for our TollandVerge Advisory company logo.2. File for our TVA company logo3. Files for Derek's signatures (for under photos) - Owen's to follow4. Photo of Derek & Owen (person in purple shirt to be cropped out)Thank you and really excited to see what everyone comes back with.Derek & Owen

Target Market(s)

Very broad - Manufacturing, Healthcare, Hospitality

Industry/Entity Type

Management Consulting

Font styles to use
Other font styles liked:
• We use Swiss721, but happy to be guided by designer

Colors
3276b5
85abd2
0355a3
333333
5c5c5c
9d9d9d
d9d9d9

Requirements
Must have
• Corporate feel
Nice to have
• Slightly friendly feel
• Our standard "blue" is (CORRECTION) - R55 G96 B146 #376092 and our standard grey is R197 G178, B179 - #B3B2B2, which we would like to keep, but other colours we are happy to be guided on. Brand guidelines attached.

```html
<!DOCTYPE html>
<html lang="en">
<head>
<meta charset="utf-8">
<title>Tolland Verge Advisory – Brochure</title>
<link href="https://fonts.googleapis.com/css2?family=Roboto+Condensed:ital,wght@0,400;0,700;1,400;1,700&family=Roboto:wght@700;900&display=swap" rel="stylesheet">
<style>
:root{
  --bg:#8a8a8a;
  --paper:#e3e4e8;
  --blue:#0355a3;
  --blue-mid:#3276b5;
  --blue-soft:#85abd2;
  --ink:#111111;
  --grey-dark:#333333;
  --grey:#5c5c5c;
  --pie-green:#33a548;
  --pie-blue:#2a97d8;
  --pie-orange:#d9531e;
  --pie-pink:#d9247a;
  --pie-brown:#8a5a2c;
}
*{box-sizing:border-box;margin:0;padding:0}
html,body{width:1200px;height:1200px;overflow:hidden;background:var(--bg)}
body{font-family:"Roboto Condensed",sans-serif;color:var(--ink)}
.board{position:absolute;left:200px;top:24px;width:800px;display:grid;grid-template-columns:400px 400px;grid-template-rows:566px 566px;row-gap:20px}
.page{position:relative;width:400px;height:566px;background:var(--paper);overflow:hidden}
.page--left{box-shadow:inset -14px 0 18px -14px rgba(0,0,0,.25)}
.page--right{box-shadow:inset 14px 0 18px -14px rgba(0,0,0,.25)}
.wordmark{font-family:"Roboto",sans-serif;font-weight:900;color:var(--ink);letter-spacing:-1px;line-height:1}
/* back cover */
.back-mark{position:absolute;left:70px;top:230px;font-size:86px}
.back-url{position:absolute;left:30px;bottom:34px;font-weight:700;font-size:13px;color:var(--blue)}
/* front cover */
.front-mark{position:absolute;right:34px;top:48px;font-size:56px}
.front-art{position:absolute;left:0;top:0;width:400px;height:566px}
/* inner pages */
.heading{position:absolute;font-weight:700;font-style:italic;font-size:17px;color:var(--ink)}
.values{position:absolute;left:28px;top:62px;width:345px;list-style:none}
.values li{position:relative;padding-left:13px;margin-bottom:9px;font-weight:700;font-style:italic;font-size:11px;line-height:1.25}
.values li::before{content:"";position:absolute;left:0;top:4px;width:6px;height:6px;border-radius:50%;background:var(--blue-mid);box-shadow:0 0 0 1.5px var(--blue-soft)}
.hl{color:var(--blue)}
.pie{position:absolute;left:70px;top:330px;width:200px;height:200px}
.pie text{font-family:"Roboto",sans-serif;font-weight:900;fill:#fff}
.folio{position:absolute;bottom:18px;right:26px;font-weight:700;font-size:10px}
.brand-label{position:absolute;left:28px;top:58px;line-height:1}
.brand-label .name{font-weight:700;font-size:18px;color:var(--ink)}
.photo-frame{position:absolute;left:28px;top:98px;width:344px;height:254px;border:3px solid var(--blue);border-radius:18px;padding:6px}
.photo{width:100%;height:100%;border-radius:12px;background:linear-gradient(135deg,#e9e9ec 0%,#b9babe 45%,#8e8f93 70%,#d2d3d6 100%)}
.signature{position:absolute;height:26px;border-bottom:1px solid var(--blue);background:linear-gradient(90deg,rgba(3,85,163,.18),rgba(3,85,163,0))}
.sig-a{left:40px;top:362px;width:110px}
.sig-b{left:230px;top:380px;width:120px}
.about-copy{position:absolute;left:28px;top:424px;width:344px;font-weight:700;font-style:italic;font-size:10px;line-height:1.3;text-align:justify}
.about-copy p{margin-bottom:6px}
</style>
</head>
<body>
<main class="board">

  <section class="page page--left back-cover">
    <div class="wordmark back-mark">TVA</div>
    <div class="back-url">http://tollandvergeadvisory.com</div>
  </section>

  <section class="page page--right front-cover">
    <svg class="front-art" viewBox="0 0 400 566">
      <defs>
        <linearGradient id="photo-tone" x1="0" y1="0" x2="1" y2="1">
          <stop offset="0" stop-color="#f2f3f6"/>
          <stop offset=".45" stop-color="#b9a99b"/>
          <stop offset=".75" stop-color="#3a4c78"/>
          <stop offset="1" stop-color="#1f2f57"/>
        </linearGradient>
      </defs>
      <circle cx="330" cy="490" r="290" fill="url(#photo-tone)" role="img" aria-label="Photo of two consultants in suits looking at a laptop together, framed by decorative orbit lines and dots"/>
    </svg>
    <div class="wordmark front-mark">TVA</div>
  </section>

  <section class="page page--left values-page">
    <h2 class="heading" style="left:28px;top:28px">Our values</h2>
    <ul class="values">
      <li>Be <span class="hl">TRUSTED</span> by our team and clients, so that our opinions are sought and our recommendations valued.</li>
      <li>Have a tight knit relationship with our clients, so we are seen as a <span class="hl">PARTNER</span> and not just supplier.</li>
      <li>Be focused on return-on-investment, but predominantly, always deliver <span class="hl">GREAT VALUE.</span></li>
      <li><span class="hl">DEVELOP &amp; INVEST IN</span> our own people to continually stay one step ahead.</li>
      <li>Work relentlessly to deliver results for our clients, but ensure we collectively <span class="hl">ENJOY THE JOURNEY.</span></li>
      <li>Take <span class="hl">SOCIAL RESPONSIBILITY</span> seriously by supporting other worthwhile organisations.</li>
    </ul>
    <svg class="pie" viewBox="0 0 200 200" role="img" aria-label="Pie chart: 50%, 25%, 15%, 10%, 10%">
      <path d="M100 100 L100 10 A90 90 0 0 1 100 190 Z" fill="var(--pie-green)"/>
      <path d="M100 100 L100 190 A90 90 0 0 1 61 181.1 Z" fill="var(--pie-brown)"/>
      <path d="M100 100 L61 181.1 A90 90 0 0 1 29.7 156.2 Z" fill="var(--pie-pink)"/>
      <path d="M100 100 L29.7 156.2 A90 90 0 0 1 10 100 Z" fill="var(--pie-orange)"/>
      <path d="M100 100 L10 100 A90 90 0 0 1 100 10 Z" fill="var(--pie-blue)"/>
      <text x="128" y="110" font-size="22">50%</text>
      <text x="38" y="60" font-size="18">25%</text>
      <text x="18" y="128" font-size="13">15%</text>
      <text x="40" y="158" font-size="9">10%</text>
      <text x="70" y="178" font-size="9">10%</text>
    </svg>
    <div class="folio">1</div>
  </section>

  <section class="page page--right about-page">
    <h2 class="heading" style="left:28px;top:28px">About Us</h2>
    <div class="brand-label"><span class="name">TollandVerge Advisory</span></div>
    <div class="photo-frame">
      <div class="photo" role="img" aria-label="Black and white photo of Derek and Owen seated at a table, smiling"></div>
    </div>
    <div class="signature sig-a" role="img" aria-label="Derek's signature"></div>
    <div class="signature sig-b" role="img" aria-label="Owen's signature"></div>
    <div class="about-copy">
      <p><span class="hl">At TVA</span> we constantly strive to deliver the best possible value for our clients. Importantly we recognize, it's our clients that define value, not us.</p>
      <p>We bring together our expertise from Kestrel Motors and our experience of working with multiple organisations to help our clients deliver results against their own individual goals.</p>
    </div>
    <div class="folio">2</div>
  </section>

</main>
</body>
</html>
```